After-School Program - End of the Year Mailing to Donors

We would like to highlight some of our accomplishments from the year and ask people to donate to our organization. We are a non-profit organization that serves underprivileged children with after school programs. We want a 6x9 flyer with printing on both sides that we can mail out soon. The flyer should be a mix of great photos, some text, and a space for mailing and return address.

Target Market(s)

regular donors

Industry/Entity Type

Education

Font styles to use
Serif

Colors

Designer to choose colors to be used in the design.

Requirements
Must have
• Photos, text, a space on one side for a mailing label, a return address, and a stamp.
Nice to have
• attractive, eye-catching
Should not have
• boring

```html
<!DOCTYPE html>
<html lang="en">
<head>
<meta charset="utf-8">
<title>Eastside Harbor Family Center – Donor Mailer</title>
<link href="https://fonts.googleapis.com/css2?family=Open+Sans:wght@300;400;700;800&family=Lato:wght@400;700&display=swap" rel="stylesheet">
<style>
  :root {
    --ink: #1d1d1d;
    --blue: #2b8fc2;
    --blue-deep: #1f79b0;
    --teal: #4f98a8;
    --yellow: #f5ea18;
    --paper: #ffffff;
    --backdrop: #e9e7e3;
    --rule: #222222;
    --stamp: #9a9a9a;
  }
  * { margin: 0; padding: 0; box-sizing: border-box; }
  html, body { width: 1046px; height: 1200px; overflow: hidden; }
  body { background: var(--backdrop); position: relative; font-family: "Lato", sans-serif; color: var(--ink); }

  .card { position: absolute; left: 132px; width: 755px; height: 504px; background: var(--paper); overflow: hidden; box-shadow: 0 3px 10px rgba(0,0,0,.18); }
  .card--front { top: 60px; }
  .card--back { top: 600px; }
  .card__shapes { position: absolute; inset: 0; }

  /* front */
  .org-mark { position: absolute; left: 559px; top: 50px; width: 160px; text-align: center; }
  .org-mark__dot { width: 60px; height: 60px; border: 3px solid var(--ink); border-radius: 50%; background: var(--yellow); margin: 0 auto 14px; }
  .org-mark__name { font-family: "Open Sans", sans-serif; font-size: 14px; line-height: 17px; font-weight: 400; letter-spacing: .2px; }

  .headline { position: absolute; right: 27px; top: 300px; text-align: right; color: var(--paper); font-family: "Open Sans", sans-serif; }
  .headline__lead { display: block; font-weight: 300; font-size: 29px; line-height: 36px; }
  .headline__main { display: block; font-weight: 800; font-size: 34px; line-height: 40px; }

  .front-web { position: absolute; right: 10px; top: 473px; font-family: "Open Sans", sans-serif; font-size: 12px; letter-spacing: 2.6px; color: var(--ink); }

  /* back */
  .about { position: absolute; left: 29px; top: 156px; width: 316px; }
  .about__title { font-family: "Lato", sans-serif; font-weight: 400; font-size: 21px; margin-bottom: 17px; margin-left: 3px; }
  .about__text { font-size: 10px; line-height: 12.6px; text-align: justify; letter-spacing: -.1px; }

  .contact { position: absolute; top: 347px; font-size: 11px; line-height: 14.5px; display: flex; gap: 6px; white-space: nowrap; }
  .contact--address { left: 36px; }
  .contact--reach { left: 206px; }
  .contact__icon { width: 10px; height: 10px; margin-top: 2px; flex: none; }
  .contact__lines { font-style: normal; }
  .contact__lines p { display: flex; gap: 6px; }

  .return-mark { position: absolute; left: 372px; top: 90px; width: 100px; text-align: center; }
  .return-mark__dot { width: 44px; height: 44px; border: 2px solid var(--ink); border-radius: 50%; background: var(--yellow); margin: 0 auto 5px; }
  .return-mark__name { font-family: "Open Sans", sans-serif; font-size: 7.5px; line-height: 9px; }

  .stamp-box { position: absolute; left: 622px; top: 88px; width: 69px; height: 79px; border: 1px solid var(--stamp); }

  .mail-line { position: absolute; left: 422px; width: 285px; border-top: 1.2px solid var(--rule); }
</style>
</head>
<body>

<section class="card card--front">
  <svg class="card__shapes" viewBox="0 0 944 630" width="755" height="504">
    <defs>
      <linearGradient id="photoFade" x1="0" y1="0" x2="1" y2="0">
        <stop offset="0" stop-color="#6f8a5c"/>
        <stop offset=".35" stop-color="#8a8fa8"/>
        <stop offset=".6" stop-color="#7f8fb0"/>
        <stop offset=".8" stop-color="#c2ccc0"/>
        <stop offset="1" stop-color="#ffffff"/>
      </linearGradient>
      <linearGradient id="photoSky" x1="0" y1="0" x2="0" y2="1">
        <stop offset="0" stop-color="#ffffff" stop-opacity=".35"/>
        <stop offset=".3" stop-color="#ffffff" stop-opacity="0"/>
        <stop offset="1" stop-color="#3c4a2c" stop-opacity=".25"/>
      </linearGradient>
      <radialGradient id="wallPhoto" cx=".5" cy=".4" r=".7">
        <stop offset="0" stop-color="#9a8b78"/>
        <stop offset="1" stop-color="#5e5248"/>
      </radialGradient>
      <radialGradient id="playPhoto" cx=".5" cy=".45" r=".7">
        <stop offset="0" stop-color="#7c8a9a"/>
        <stop offset="1" stop-color="#4a4a3c"/>
      </radialGradient>
      <radialGradient id="festivePhoto" cx=".5" cy=".6" r=".7">
        <stop offset="0" stop-color="#b04a5a"/>
        <stop offset="1" stop-color="#2e3a6a"/>
      </radialGradient>
      <linearGradient id="blueBand" x1="0" y1="0" x2="1" y2="1">
        <stop offset="0" stop-color="var(--blue-deep)"/>
        <stop offset=".6" stop-color="#55acd2"/>
        <stop offset="1" stop-color="var(--blue)"/>
      </linearGradient>
    </defs>
    <g role="img" aria-label="Group photo of smiling children with a program leader outdoors in a park">
      <rect x="0" y="0" width="730" height="630" fill="url(#photoFade)"/>
      <rect x="0" y="0" width="730" height="630" fill="url(#photoSky)"/>
    </g>
    <path d="M0 630 L0 600 C160 520 360 360 560 330 C700 305 830 290 944 292 L944 630 Z" fill="var(--ink)"/>
    <path d="M0 630 L0 612 C170 535 370 380 565 345 C705 320 830 306 944 308 L944 630 Z" fill="var(--yellow)"/>
    <path d="M0 630 L0 625 C175 548 380 392 570 358 C710 334 832 322 944 326 L944 630 Z" fill="url(#blueBand)"/>
    <path d="M330 630 C520 575 760 540 944 552 L944 630 Z" fill="var(--ink)"/>
    <path d="M370 630 C560 585 780 560 944 572 L944 630 Z" fill="var(--yellow)"/>
    <circle cx="113" cy="525" r="112" fill="url(#wallPhoto)" stroke="#fff" stroke-width="6" role="img" aria-label="Photo of children sitting together on a low wall"/>
    <circle cx="285" cy="435" r="88" fill="url(#playPhoto)" stroke="#fff" stroke-width="6" role="img" aria-label="Photo of children playing outdoors with a volunteer"/>
    <circle cx="435" cy="375" r="75" fill="url(#festivePhoto)" stroke="#fff" stroke-width="6" role="img" aria-label="Photo of two girls wearing festive reindeer headbands"/>
  </svg>

  <div class="org-mark">
    <div class="org-mark__dot"></div>
    <p class="org-mark__name">EASTSIDE HARBOR<br>FAMILY CENTER</p>
  </div>

  <h1 class="headline">
    <span class="headline__lead">BUILDING PROGRAMS</span>
    <span class="headline__main">FOR CHILDREN,</span>
    <span class="headline__main">YOUTH AND FAMILIES</span>
  </h1>

  <p class="front-web">www.brightsteps-kids.org</p>
</section>

<section class="card card--back">
  <svg class="card__shapes" viewBox="0 0 944 630" width="755" height="504">
    <rect x="0" y="0" width="944" height="140" fill="var(--yellow)"/>
    <path d="M0 70 C120 120 250 130 420 92 C600 48 800 22 944 88 L944 630 L0 630 Z" fill="var(--paper)"/>
    <path d="M120 106 C300 138 450 82 600 48 C700 28 780 30 820 40 C700 36 560 72 420 112 C300 142 200 132 120 106 Z" fill="var(--teal)"/>
    <path d="M280 540 C520 612 800 585 944 462 L944 630 L280 630 Z" fill="var(--teal)"/>
    <path d="M0 630 V545 C120 505 260 510 420 560 C600 620 800 612 944 545 V630 Z" fill="var(--paper)"/>
    <path d="M0 630 V553 C120 513 260 518 420 568 C600 628 800 620 944 553 V630 Z" fill="var(--ink)"/>
  </svg>

  <div class="return-mark">
    <div class="return-mark__dot"></div>
    <p class="return-mark__name">EASTSIDE HARBOR<br>FAMILY CENTER</p>
  </div>

  <div class="stamp-box"></div>

  <article class="about">
    <h2 class="about__title">ABOUT US</h2>
    <p class="about__text">Eastside Harbor Family Center is in the middle of its 24th year of ministry and we need your help to finish our year strong! We need another $35,000 from our individual donors to help us meet our budget. We serve over 150 children each day at our four sites with a unique mix of homework help, a focus on literacy, enrichment classes - including music lessons, and a caring environment based on God's love. Please help us continue to impact children and families through our high quality faith-based educational programs.</p>
  </article>

  <div class="contact contact--address">
    <svg class="contact__icon" viewBox="0 0 10 10"><path d="M5 .8a3.2 3.2 0 0 0-3.2 3.2C1.8 6.4 5 9.4 5 9.4S8.2 6.4 8.2 4A3.2 3.2 0 0 0 5 .8Z" fill="none" stroke="currentColor" stroke-width="1"/><circle cx="5" cy="4" r="1.1" fill="none" stroke="currentColor" stroke-width=".9"/></svg>
    <address class="contact__lines">418 W. Linden Ave.<br>Alder Springs, CA 90000</address>
  </div>

  <div class="contact contact--reach">
    <div class="contact__lines">
      <p><svg class="contact__icon" viewBox="0 0 10 10"><path d="M2.3 .8 3.8 2.6 2.9 3.7C3.5 5 4.9 6.5 6.3 7.1L7.4 6.2 9.2 7.7 8.3 9.1C4.6 8.9 1.1 5.4.9 1.7Z" fill="currentColor"/></svg>(555) 013-2740</p>
      <p><svg class="contact__icon" viewBox="0 0 10 10" fill="none" stroke="currentColor" stroke-width=".9"><circle cx="5" cy="5" r="4.2"/><ellipse cx="5" cy="5" rx="1.8" ry="4.2"/><path d="M.8 5h8.4"/></svg>www.brightsteps-kids.org</p>
    </div>
  </div>

  <div class="mail-line" style="top:312px"></div>
  <div class="mail-line" style="top:352px"></div>
  <div class="mail-line" style="top:386px"></div>
</section>

</body>
</html>
```